Web Design for High End Baby Products Gear

We have some work from a designer that just didn't meet standards despite weeks of back and forth. We need someone who can come up with creative colors/fonts/etc. to make the site "pop" and give a clean, inviting feel.

We need three pages designed:

1. Home
2. Category Landing Page
3. Product Detail Page

The current site is www.HappyWheelWalks.com

Please DO NOT use current site for inspiration.

The layout should follow pretty close to what we have attached.

We were not even pleased with the logo so for now we are just concentrating on the colors and aesthetic feel of the site. You can use a nice typography type logo. We will probably have the logo done at a later time. Or if you have any ideas please feel free to submit as it may increase chances of winning design. The layout is pretty much done with the product page layout approved by our paid search people.

This is isn't where you need to spend a lot of time with general layout as it is already pretty much complete but you are free to deviate or make suggestions if you think it will help.

Reason: I haven't been able to provide adequate feedback and want to spend appropriate amount of time doing so.

I posted the set of PSD files that the previous designer completed.  We were not happy with the outcome of this.

I said in my brief "Here are a few like companies:

www.pramvault.com
www.buggynest.com
www.tiddlytopkids.com
www.kplums.com
www.wrenandtilly.com
www.doravimo.com"

What I meant was that these were similar companies to our company with respect to product/customer demographic/etc.

Reason: We have found a few that we really like and are working to determine which designs to continue with.

Thank you for your patience.

Reason: Waiting on feedback from a couple of designers so extending deadline

Thank you all.  We received several designs we really liked.  A couple stood out more than others as they seemed to hit the target on the first go around based on our brief and sample sites submitted.

There are several designers we would like to work with in the future as well as we have about 40 domains we will be developing.

Thank you.

Target Market(s)

Target Market: Female, typically 25-40 yrs old, probably married, probably career minded OR middle to upper middle income (some of our strollers are $500-$1,200), expecting mom or mom, some might have two stroller aged (double strollers). Some of our products are QUALITY (ZEK for jogging or running) or QUALITY with STYLE (Quillaro), but the truth is that this is a WANT not a need. Sure people need A stroller but not a $900 Tessel Stroller. So they have a combination of want and need coupled with ability to pay.

Brand Personality:
Definitely clean, crisp and modern. We want it to “POP” but in color and style. But I guess more directly is we want to be seen as THE or ONE of THE authorities on upper end strollers. Where you can get individual assistance, stroller consultations (yes people call in with their needs and ask advice) and personalized service as opposed to a “big box” type place that tries to be everything to everyone and when you call them you get some guy in a cubicle answering the phone that held his baby niece once. So when someone hits our site or walks into our showroom, they need to know they are in the right place.

Industry/Entity Type

Baby

Requirements
Must have
• Must a clean crisp color scheme, easy to ready, focused on products. Must instill authority, credibility, usability and be simple and uncluttered. Fonts and colors must complement each other to achieve the above.

We need three main images as well for the home page as they will be sliding/rotating images.

Backend is built in Magento so design must conform to that platform.

We retain exlusive rights to the design and all files
Nice to have
• Please see attached word file for more info.

Here are some sites we like:

www.tinyharbor.com
http://www.cubnook.com/
http://www.dapwick.com/
http://www.vemakids.com/index.php
http://www.fernwax.com/
http://www.tana-lume.com/
http://www.grelby.com/
http://www.cardsmithpartners.com/

Keep in mind that I may just like only something about the above sites and not everything. It may be color, it may be layout , font color, use of text on home page, but something about them stands out.

Here are a few like companies:

www.pramvault.com
www.buggynest.com
www.tiddlytopkids.com
www.kplums.com
www.wrenandtilly.com
www.doravimo.com
Should not have
• old dated styles, nothing "frilly"

```html
<!DOCTYPE html>
<html lang="en">
<head>
<meta charset="utf-8">
<title>Baby Products – Home</title>
<link rel="stylesheet" href="https://fonts.googleapis.com/css2?family=Ubuntu:wght@400;500;700&family=Noto+Sans:wght@400;700&display=swap">
<style>
:root{
  --pink:#e8238f;
  --pink-light:#f56bb4;
  --blue:#1f8fe0;
  --green:#6aae2a;
  --olive:#7a9a1a;
  --ink:#222;
  --muted:#555;
  --line:#d6d6d6;
  --panel:#f4f4f4;
  --white:#fff;
}
*{box-sizing:border-box;margin:0;padding:0}
html,body{width:1160px;height:1200px;overflow:hidden;background:var(--white)}
body{position:relative;font-family:"Noto Sans",Tahoma,sans-serif;color:var(--ink);font-size:11px}
a{color:inherit;text-decoration:none}
.abs{position:absolute}

/* header */
.brand{left:143px;top:30px}
.brand-name{font-family:"Ubuntu",sans-serif;font-weight:500;font-size:44px;line-height:46px;color:var(--pink);letter-spacing:-1px}
.brand-tag{font-size:11.5px;color:#333;margin-left:100px;margin-top:-4px}
.perks{left:471px;top:12px;list-style:none}
.perks li{display:flex;align-items:center;gap:7px;height:19px;font-size:11.5px;color:#333}
.account{left:669px;top:32px;display:flex;align-items:center;gap:6px;font-weight:700;font-size:11.5px;color:var(--pink)}
.prefs{left:713px;top:58px;display:flex;gap:8px;align-items:center;font-size:11.5px;color:#333}
.select{width:74px;height:14px;border:1px solid #bbb;font-size:9.5px;color:#999;padding-left:3px;line-height:12px;position:relative;margin-right:12px}
.select::after{content:"";position:absolute;right:0;top:0;width:13px;height:12px;border-left:1px solid #bbb;background:linear-gradient(#fff,#ddd)}

/* nav */
.nav{left:140px;top:98px;width:880px;height:47px;border:1px solid var(--line);border-radius:4px;background:linear-gradient(#fff,#f3f3f3);display:flex;align-items:center}
.nav a{font-weight:700;font-size:12px;padding:0 16px;border-right:1px solid #555;line-height:20px;color:#222}
.nav a.active{color:var(--pink)}
.nav a:nth-child(7){border-right:none}
.search{margin-left:auto;margin-right:12px;display:flex;align-items:center;gap:12px}
.search span{display:block;width:132px;height:20px;border:1px solid #ccc;border-radius:3px;color:#aaa;font-size:11px;line-height:18px;padding-left:6px}

/* promos */
.box{border:1px solid var(--line);border-radius:4px;overflow:hidden;background:var(--white)}
.offer{left:140px;top:155px;width:175px;height:342px;background:linear-gradient(#f8f8f8,#fff)}
.offer-badge{position:absolute;left:21px;top:16px;width:138px;height:38px;border-radius:50%;background:var(--pink);border:3px solid #fff;box-shadow:0 0 0 1px #ddd;color:#fff;font-family:"Ubuntu",sans-serif;font-size:15px;text-align:center;line-height:32px}
.offer-text{position:absolute;top:66px;width:100%;text-align:center;color:var(--olive);font-weight:700;font-size:11.5px;line-height:14px}
.offer-text u{display:block;color:#555}
.offer-photo{position:absolute;left:0;top:110px;width:100%;height:232px;background:linear-gradient(160deg,#dfe3ea,#8a8f9d 45%,#2a2b36 75%,#bfc2c8)}
.hero{left:323px;top:155px;width:697px;height:201px;background:linear-gradient(90deg,#fff 32%,#f3f1ee 45%,#fff 52%)}
.hero-title{position:absolute;left:54px;top:44px;font-family:"Ubuntu",sans-serif;font-size:58px;line-height:52px;color:var(--blue)}
.hero-sub{position:absolute;left:59px;top:163px;font-size:9.5px;letter-spacing:.5px;display:flex;align-items:center;gap:6px}
.hero-photo{position:absolute;right:0;top:0;width:310px;height:201px;background:linear-gradient(200deg,#b8b0a4,#e9e3d8 40%,#2b2b2b 65%,#d7cab2 85%)}
.tile{top:365px;width:219px;height:131px}
.tile-title{position:absolute;left:20px;top:28px;font-family:"Ubuntu",sans-serif;font-size:23px;line-height:23px;color:var(--pink);font-style:normal}
.tile-link{position:absolute;left:20px;top:88px;display:flex;align-items:center;gap:6px;font-size:12px;text-decoration:underline}
.tile-photo{position:absolute;right:0;top:0;width:112px;height:131px}

/* sidebar */
.side{left:140px;width:175px;background:linear-gradient(#f3f3f3,#fff 40%)}
.side h3{font-family:"Noto Sans",sans-serif;font-size:12.5px;color:var(--blue);padding:17px 0 10px 18px}
.side ul{list-style:none;margin:0 28px 0 16px}
.side li{display:flex;align-items:center;gap:7px;height:25.4px;border-bottom:1px dotted #ccc;font-size:11px;color:#333}
.subscribe{left:140px;top:1029px;width:175px;height:94px}
.subscribe .env{position:absolute;left:9px;top:8px;width:58px;height:44px;background:linear-gradient(#fafafa,#cfd7dd);border:1px solid #ccc;border-radius:3px}
.subscribe strong{position:absolute;left:75px;top:18px;font-family:"Ubuntu",sans-serif;font-weight:400;font-size:19px}
.subscribe small{position:absolute;left:75px;top:42px;font-size:10px;color:#555}
.subscribe .field{position:absolute;left:8px;top:67px;width:120px;height:17px;border:1px solid #ccc;border-radius:3px}
.subscribe .go{position:absolute;left:139px;top:63px;width:24px;height:24px;border-radius:50%;background:var(--pink);color:#fff;font-size:9px;text-align:center;line-height:24px}

/* products */
.card{width:154px}
.card-img{height:196px;border:1px solid var(--line);border-radius:4px;background:#fff;position:relative}
.card-img div{position:absolute;inset:12px 14px}
.card-title{margin-top:12px;font-size:11.5px;line-height:13px;color:#222}
.card-title b{font-weight:700}
.card-price{margin-top:8px;font-weight:700;font-size:12.5px}
.btn{display:inline-block;margin-top:10px;width:82px;height:24px;border-radius:4px;background:linear-gradient(var(--pink-light),var(--pink));color:#fff;font-weight:700;font-size:11.5px;text-align:center;line-height:24px;letter-spacing:.3px}
.c1{left:323px}.c2{left:504px}.c3{left:685px}.c4{left:866px}
.r1{top:510px}.r2{top:827px}
.red{background:linear-gradient(160deg,#e33b3b,#9b1d2a 55%,#d8d8d8)}
.yellow{background:linear-gradient(160deg,#f2d522,#d4a419 55%,#8b8b8b)}
.blue{background:linear-gradient(160deg,#3f86c8,#2b5d96 55%,#3b3b3b)}
.cream{background:linear-gradient(160deg,#e9e1cf,#c9bca4 55%,#4a4a4a)}

/* footer */
.footer{left:140px;top:1131px;width:880px;height:47px;border:1px solid var(--line);border-radius:4px;background:linear-gradient(#fff,#f3f3f3)}
.pay{position:absolute;left:30px;top:12px;display:flex;gap:3px}
.pay span{width:42px;height:23px;border:1px solid #999;font-size:9px;font-weight:700;text-align:center;line-height:21px;color:#1f4a8c;background:#fff}
.foot-links{position:absolute;left:0;right:0;top:10px;text-align:center;font-size:11px;color:#222;word-spacing:1px}
.foot-copy{position:absolute;left:0;right:0;top:27px;text-align:center;font-size:8.5px;color:#222}
.social{position:absolute;right:52px;top:13px;display:flex;gap:14px;font-size:11px;font-weight:700;color:var(--blue)}
.social span{display:flex;align-items:center;gap:4px}
.social i{display:block;width:12px;height:12px;border-radius:50%;background:var(--blue)}
</style>
</head>
<body>

<header>
  <div class="abs brand">
    <div class="brand-name">Baby Products</div>
    <div class="brand-tag">Get your baby&nbsp; product right here.</div>
  </div>
  <ul class="abs perks">
    <li><svg width="15" height="12" viewBox="0 0 15 12"><path d="M1 6l4 4 9-9" fill="none" stroke="#6aae2a" stroke-width="3"/></svg>365 Day Returns</li>
    <li><svg width="15" height="12" viewBox="0 0 15 12"><path d="M1 6l4 4 9-9" fill="none" stroke="#6aae2a" stroke-width="3"/></svg>Free Shipping*</li>
    <li><svg width="15" height="12" viewBox="0 0 15 12"><path d="M1 6l4 4 9-9" fill="none" stroke="#6aae2a" stroke-width="3"/></svg>No Sales Tax</li>
    <li><svg width="15" height="12" viewBox="0 0 15 12"><path d="M1 6l4 4 9-9" fill="none" stroke="#6aae2a" stroke-width="3"/></svg>Price Match Guarantee</li>
  </ul>
  <div class="abs account">
    <svg width="22" height="18" viewBox="0 0 22 18"><path d="M1 2h4l3 10h11l2-7H7" fill="none" stroke="#1f8fe0" stroke-width="2"/><circle cx="9" cy="15.5" r="1.8" fill="#1f8fe0"/><circle cx="17" cy="15.5" r="1.8" fill="#1f8fe0"/></svg>
    <span>My Shopping Cart l Registry l Checkout l My Account</span>
  </div>
  <div class="abs prefs">
    <span>Language</span><span class="select">English</span>
    <span>Currency</span><span class="select">US $</span>
  </div>
</header>

<nav class="abs nav">
  <a class="active" href="#">Home</a>
  <a href="#">Sale Gift</a>
  <a href="#">Registry</a>
  <a href="#">Gift Cards</a>
  <a href="#">Contact Us</a>
  <a href="#">Store Location</a>
  <a href="#">Blog</a>
  <div class="search">
    <span>Search store</span>
    <svg width="22" height="22" viewBox="0 0 22 22"><circle cx="9" cy="9" r="6.5" fill="none" stroke="#888" stroke-width="2.5"/><path d="M14 14l6 6" stroke="#666" stroke-width="3"/></svg>
  </div>
</nav>

<section class="abs box offer">
  <div class="offer-badge">Special Offer</div>
  <div class="offer-text">Get Latest Best<br>Baby products<u>details</u></div>
  <div class="offer-photo" role="img" aria-label="Photo of a jogging stroller parked by a wall"></div>
</section>

<section class="abs box hero">
  <div class="hero-title">Best Baby<br>Stroller</div>
  <div class="hero-sub">Take for your baby
    <svg width="30" height="16" viewBox="0 0 30 16"><rect x="1" y="5" width="17" height="7" fill="#f0b400"/><rect x="18" y="2" width="10" height="10" rx="1" fill="#1f8fe0"/><circle cx="7" cy="13" r="2.5" fill="#555"/><circle cx="23" cy="13" r="2.5" fill="#555"/></svg>
  </div>
  <div class="hero-photo" role="img" aria-label="Close-up photo of a stroller handlebar and canopy"></div>
</section>

<section class="abs box tile" style="left:323px">
  <div class="tile-title">Baby<br>Stroller</div>
  <a class="tile-link" href="#"><svg width="14" height="14" viewBox="0 0 14 14"><circle cx="7" cy="7" r="6" fill="#eee" stroke="#bbb"/><path d="M5.5 4l3 3-3 3" fill="none" stroke="#6aae2a" stroke-width="1.6"/></svg>Details</a>
  <div class="tile-photo" role="img" aria-label="Photo of a red stroller seat" style="background:linear-gradient(90deg,#fff,#f5a0ae 40%,#e23a55 75%,#c9c9c9)"></div>
</section>
<section class="abs box tile" style="left:562px">
  <div class="tile-title">Baby<br>Stroller</div>
  <a class="tile-link" href="#"><svg width="14" height="14" viewBox="0 0 14 14"><circle cx="7" cy="7" r="6" fill="#eee" stroke="#bbb"/><path d="M5.5 4l3 3-3 3" fill="none" stroke="#6aae2a" stroke-width="1.6"/></svg>Details</a>
  <div class="tile-photo" role="img" aria-label="Photo of a blue and red stroller canopy" style="background:linear-gradient(90deg,#fff,#8fb4d4 35%,#3b6fa6 60%,#c0392b 90%)"></div>
</section>
<section class="abs box tile" style="left:801px">
  <div class="tile-title">Baby<br>Stroller</div>
  <a class="tile-link" href="#"><svg width="14" height="14" viewBox="0 0 14 14"><circle cx="7" cy="7" r="6" fill="#eee" stroke="#bbb"/><path d="M5.5 4l3 3-3 3" fill="none" stroke="#6aae2a" stroke-width="1.6"/></svg>Details</a>
  <div class="tile-photo" role="img" aria-label="Photo of a store shelf with strollers and toys" style="background:linear-gradient(90deg,#fff,#b9c7d8 35%,#2f4f7a 60%,#8a6a3a 90%)"></div>
</section>

<aside class="abs box side" style="top:510px;height:339px">
  <h3>Categories</h3>
  <ul>
    <li><span>→</span>Tot Trotter</li>
    <li><span>→</span>ZEK Stroller</li>
    <li><span>→</span>Quillaro Stroller</li>
    <li><span>→</span>Breezeroll Stroller</li>
    <li><span>→</span>Halden Strollers</li>
    <li><span>→</span>Ivvo Strollers</li>
    <li><span>→</span>Nanas and Nonos</li>
    <li><span>→</span>Ridge Rover</li>
    <li><span>→</span>Tessel Baby Stroller</li>
    <li><span>→</span>Pip and Tobs</li>
    <li style="border:none"><span>→</span>Pop Star Stroller</li>
  </ul>
</aside>

<aside class="abs box side" style="top:854px;height:169px">
  <h3>Best Sellers</h3>
  <ul>
    <li><svg width="12" height="12" viewBox="0 0 12 12"><circle cx="6" cy="6" r="5" fill="none" stroke="#1f8fe0"/><path d="M4 6h4M6 4l2 2-2 2" fill="none" stroke="#1f8fe0"/></svg>Tot Trotter</li>
    <li><svg width="12" height="12" viewBox="0 0 12 12"><circle cx="6" cy="6" r="5" fill="none" stroke="#1f8fe0"/><path d="M4 6h4M6 4l2 2-2 2" fill="none" stroke="#1f8fe0"/></svg>ZEK Stroller</li>
    <li><svg width="12" height="12" viewBox="0 0 12 12"><circle cx="6" cy="6" r="5" fill="none" stroke="#1f8fe0"/><path d="M4 6h4M6 4l2 2-2 2" fill="none" stroke="#1f8fe0"/></svg>Quillaro Stroller</li>
    <li><svg width="12" height="12" viewBox="0 0 12 12"><circle cx="6" cy="6" r="5" fill="none" stroke="#1f8fe0"/><path d="M4 6h4M6 4l2 2-2 2" fill="none" stroke="#1f8fe0"/></svg>Breezeroll Stroller</li>
    <li style="border:none"><svg width="12" height="12" viewBox="0 0 12 12"><circle cx="6" cy="6" r="5" fill="none" stroke="#1f8fe0"/><path d="M4 6h4M6 4l2 2-2 2" fill="none" stroke="#1f8fe0"/></svg>Halden Strollers</li>
  </ul>
</aside>

<section class="abs box subscribe">
  <div class="env" role="img" aria-label="Envelope illustration"></div>
  <strong>Subscribe</strong>
  <small>for a news letter</small>
  <div class="field"></div>
  <div class="go">Go!</div>
</section>

<main>
  <article class="abs card c1 r1"><div class="card-img"><div class="red" role="img" aria-label="Red stroller with silver frame"></div></div><p class="card-title"><b>Tot Trotter</b> dummy the product best quality</p><p class="card-price">$0.99</p><a class="btn" href="#">Add to Cart</a></article>
  <article class="abs card c2 r1"><div class="card-img"><div class="yellow" role="img" aria-label="Yellow three-wheel jogging stroller"></div></div><p class="card-title"><b>Tot Trotter</b> dummy the product best quality</p><p class="card-price">$0.99</p><a class="btn" href="#">Add to Cart</a></article>
  <article class="abs card c3 r1"><div class="card-img"><div class="blue" role="img" aria-label="Blue compact stroller"></div></div><p class="card-title"><b>Tot Trotter</b> dummy the product best quality</p><p class="card-price">$0.99</p><a class="btn" href="#">Add to Cart</a></article>
  <article class="abs card c4 r1"><div class="card-img"><div class="cream" role="img" aria-label="Cream pram with bassinet"></div></div><p class="card-title"><b>Tot Trotter</b> dummy the product best quality</p><p class="card-price">$0.99</p><a class="btn" href="#">Add to Cart</a></article>

  <article class="abs card c1 r2"><div class="card-img"><div class="red" role="img" aria-label="Red stroller with silver frame"></div></div><p class="card-title"><b>Tot Trotter</b> dummy the product best quality</p><p class="card-price">$0.99</p><a class="btn" href="#">Add to Cart</a></article>
  <article class="abs card c2 r2"><div class="card-img"><div class="yellow" role="img" aria-label="Yellow three-wheel jogging stroller"></div></div><p class="card-title"><b>Tot Trotter</b> dummy the product best quality</p><p class="card-price">$0.99</p><a class="btn" href="#">Add to Cart</a></article>
  <article class="abs card c3 r2"><div class="card-img"><div class="blue" role="img" aria-label="Blue compact stroller"></div></div><p class="card-title"><b>Tot Trotter</b> dummy the product best quality</p><p class="card-price">$0.99</p><a class="btn" href="#">Add to Cart</a></article>
  <article class="abs card c4 r2"><div class="card-img"><div class="cream" role="img" aria-label="Cream pram with bassinet"></div></div><p class="card-title"><b>Tot Trotter</b> dummy the product best quality</p><p class="card-price">$0.99</p><a class="btn" href="#">Add to Cart</a></article>
</main>

<footer class="abs footer">
  <div class="pay"><span>Cardo</span><span>Mercard</span><span>PayNest</span></div>
  <div class="foot-links">Homepage&nbsp; | &nbsp;Blog&nbsp; | &nbsp;Products&nbsp; | &nbsp;MyAccount&nbsp; | &nbsp;Checkout</div>
  <div class="foot-copy">Copyright © 2011 High &amp; baby Store &nbsp;|&nbsp; Privacy Policy &nbsp;|&nbsp; Terms Of Use</div>
  <div class="social"><span><i></i>Friendly</span><span><i></i>Chirper</span></div>
</footer>

</body>
</html>
```